New Energy Drink

*Name, Logo, Flatlay, and V5 Mockup design of a new energy drink*
We are a current RTD (ready to drink) company looking to expand into the Energy market. We are not sure if we will stick with our parent company name or go a completely different direction. That's where you come in.
Get creative. Come up with a name, design a logo, and create the look and feel of our next big product. We want fun, bright, and forward-thinking designs. Don't think Zipfox and tundra, but more along the lines of Crane, V5, and Tilt as our proposed target market is in the same 18-25 demographic.
The only request is the Term "With Super Caffeine" appear somewhere on the visible label. A V5 can render is attached. Please provide a Lay Flat and a Rendered Can together when submitting your designs.
FYI, the design brief is just a generic template. DO NOT USE the "grunge" or "brick" as a reference when creating your designs. We are offering a $1,000 prize to the winning designer. So please, really think this through. 1 great design is better than 5 quick designs. Good Luck!
18-25

```html
<!DOCTYPE html>
<html lang="en">
<head>
<meta charset="utf-8">
<title>Zynko Energy Drinks – Label Flatlay</title>
<link href="https://fonts.googleapis.com/css2?family=Archivo+Black&family=Montserrat:wght@600;800&display=swap" rel="stylesheet">
<style>
  :root {
    --ink: #111111;
    --board: #1f1f1f;
    --lime: #a4d13a;
    --banana: #f2e31b;
    --berry: #ec1f86;
    --paper: #ffffff;
    --stage-top: #b5b5b5;
    --stage-bottom: #7d7d7d;
  }
  * { box-sizing: border-box; margin: 0; padding: 0; }
  html, body { width: 1200px; height: 2316px; overflow: hidden; }
  body { background: var(--board); font-family: "Montserrat", Arial, sans-serif; position: relative; }

  .label { position: absolute; display: flex; overflow: hidden; }
  .label--lemon { left: 40px; top: 40px; width: 1120px; height: 360px; --flavor: var(--lime); }
  .label--banana { left: 40px; top: 450px; width: 545px; height: 240px; --flavor: var(--banana); }
  .label--berry { left: 615px; top: 450px; width: 545px; height: 240px; --flavor: var(--berry); }

  .panel { position: relative; height: 100%; }
  .panel--front { width: 27%; background: var(--flavor); }
  .panel--hero { width: 46%; background: var(--ink); }
  .panel--info { width: 27%; background: var(--flavor); }

  .brand-name {
    font-family: "Archivo Black", Arial, sans-serif;
    color: var(--ink);
    position: absolute; left: 50%; top: 44%;
    transform: translate(-50%, -50%) rotate(-90deg);
    line-height: 1; white-space: nowrap;
  }
  .label--lemon .brand-name { font-size: 72px; }
  .label--banana .brand-name, .label--berry .brand-name { font-size: 42px; }

  .hero-block { position: absolute; right: 0; bottom: 0; width: 42%; height: 60%; background: var(--flavor); }

  .tagline { position: absolute; color: var(--flavor); font-weight: 800; line-height: 1; text-transform: uppercase; }
  .tagline small { display: block; color: var(--paper); text-transform: none; font-weight: 600; }
  .label--lemon .tagline { left: 36px; top: 60px; font-size: 44px; }
  .label--lemon .tagline small { font-size: 22px; margin-bottom: 8px; }
  .label--banana .tagline, .label--berry .tagline { left: 18px; top: 36px; font-size: 22px; }
  .label--banana .tagline small, .label--berry .tagline small { font-size: 11px; margin-bottom: 4px; }

  .volume { position: absolute; color: var(--paper); font-weight: 800; }
  .label--lemon .volume { left: 36px; bottom: 26px; font-size: 24px; }
  .label--banana .volume, .label--berry .volume { left: 18px; bottom: 16px; font-size: 13px; }

  .flavor-name { position: absolute; left: 0; right: 0; text-align: center; color: var(--ink); font-weight: 800; text-transform: uppercase; }
  .label--lemon .flavor-name { bottom: 26px; font-size: 20px; }
  .label--banana .flavor-name, .label--berry .flavor-name { bottom: 14px; font-size: 11px; text-transform: none; }

  .flavor-note { position: absolute; left: 14px; top: 12px; font-size: 14px; font-weight: 600; color: var(--ink); }

  .facts {
    position: absolute; background: var(--paper); color: var(--ink);
    border: 2px solid var(--ink); font-weight: 600;
  }
  .label--lemon .facts { right: 16px; top: 16px; width: 260px; padding: 8px 10px; font-size: 11px; }
  .label--banana .facts, .label--berry .facts { right: 8px; top: 10px; width: 132px; padding: 4px 6px; font-size: 6px; }
  .facts h3 { font-family: "Archivo Black", Arial, sans-serif; font-weight: 400; font-size: 2em; line-height: 1; border-bottom: 4px solid var(--ink); padding-bottom: 3px; }
  .facts .row { display: flex; justify-content: space-between; border-bottom: 1px solid var(--ink); padding: 2px 0; }
  .facts .row--big { font-size: 1.8em; font-weight: 800; border-bottom-width: 3px; }

  .price { position: absolute; background: var(--paper); color: var(--ink); border: 2px solid var(--ink); font-weight: 800; text-align: center; }
  .label--lemon .price { right: 16px; bottom: 20px; width: 130px; font-size: 18px; padding: 2px 0; }

  .brand-lockup { position: absolute; left: 0; right: 0; top: 1150px; text-align: center; color: var(--paper); }
  .brand-lockup .wordmark { font-family: "Archivo Black", Arial, sans-serif; font-size: 120px; line-height: 1; }
  .brand-lockup .descriptor { font-weight: 800; font-size: 34px; letter-spacing: 12px; margin-top: 6px; }

  .stage {
    position: absolute; left: 0; top: 1440px; width: 1200px; height: 876px;
    background: linear-gradient(180deg, var(--stage-top), var(--stage-bottom));
  }
  .stage .wordmark-small { position: absolute; right: 60px; top: 70px; font-family: "Archivo Black", Arial, sans-serif; font-size: 44px; color: var(--ink); }
</style>
</head>
<body>

<section class="label label--lemon">
  <div class="panel panel--front">
    <span class="flavor-note">zesty</span>
    <span class="brand-name">ZYNKO</span>
    <span class="flavor-name">Lemon Zynk</span>
  </div>
  <div class="panel panel--hero">
    <span class="hero-block"></span>
    <p class="tagline"><small>With</small>Super<br>Caffeine</p>
    <span class="volume">16 FL OZ</span>
  </div>
  <div class="panel panel--info">
    <div class="facts">
      <h3>Nutrition Facts</h3>
      <div class="row"><span>Serving Size</span><span>1 can</span></div>
      <div class="row row--big"><span>Calories</span><span>230</span></div>
      <div class="row"><span>Total Fat</span><span>0g</span></div>
      <div class="row"><span>Sodium</span><span>95mg</span></div>
      <div class="row"><span>Total Carbs</span><span>58g</span></div>
      <div class="row"><span>Sugars</span><span>56g</span></div>
      <div class="row"><span>Caffeine</span><span>160mg</span></div>
    </div>
    <span class="price">$5</span>
  </div>
</section>

<section class="label label--banana">
  <div class="panel panel--front">
    <span class="brand-name">ZYNKO</span>
    <span class="flavor-name">Banana Power</span>
  </div>
  <div class="panel panel--hero">
    <span class="hero-block"></span>
    <p class="tagline"><small>With</small>Super<br>Caffeine</p>
    <span class="volume">16 FL OZ</span>
  </div>
  <div class="panel panel--info">
    <div class="facts">
      <h3>Nutrition Facts</h3>
      <div class="row"><span>Serving Size</span><span>1 can</span></div>
      <div class="row row--big"><span>Calories</span><span>230</span></div>
      <div class="row"><span>Total Carbs</span><span>58g</span></div>
      <div class="row"><span>Caffeine</span><span>160mg</span></div>
    </div>
  </div>
</section>

<section class="label label--berry">
  <div class="panel panel--front">
    <span class="brand-name">ZYNKO</span>
    <span class="flavor-name">Berry Punch</span>
  </div>
  <div class="panel panel--hero">
    <span class="hero-block"></span>
    <p class="tagline"><small>With</small>Super<br>Caffeine</p>
    <span class="volume">16 FL OZ</span>
  </div>
  <div class="panel panel--info">
    <div class="facts">
      <h3>Nutrition Facts</h3>
      <div class="row"><span>Serving Size</span><span>1 can</span></div>
      <div class="row row--big"><span>Calories</span><span>230</span></div>
      <div class="row"><span>Total Carbs</span><span>58g</span></div>
      <div class="row"><span>Caffeine</span><span>160mg</span></div>
    </div>
  </div>
</section>

<header class="brand-lockup">
  <div class="wordmark">ZYNKO</div>
  <div class="descriptor">ENERGY DRINKS</div>
</header>

<section class="stage" role="img" aria-label="Rendered cans of Banana Power and Lemon Zynk lying on a grey surface">
  <span class="wordmark-small">ZYNKO</span>
</section>

</body>
</html>
```